Letter Head Design

I need a letter head design based on my company logo that I attached.
Include phone number: (403)582-4316
Address: 347 14th Avenue NE, Calgary, Alberta, Canada, T3K 4R8

Industry/Entity Type

It Company

```html
<!DOCTYPE html>
<html lang="en">
<head>
<meta charset="utf-8">
<title>BrightRoom Interiors – Letterhead</title>
<link href="https://fonts.googleapis.com/css2?family=Quicksand:wght@500;700&display=swap" rel="stylesheet">
<style>
  :root {
    --brand-blue: #1f4f9c;
    --brand-green: #5aad3f;
    --ink: #1b1b1b;
    --paper: #ffffff;
  }
  * { margin: 0; padding: 0; box-sizing: border-box; }
  html, body { width: 927px; height: 1200px; overflow: hidden; background: var(--paper); }
  .letterhead {
    position: relative;
    width: 927px;
    height: 1200px;
    background: var(--paper);
    font-family: "Quicksand", sans-serif;
    color: var(--ink);
  }
  .frame-shapes { position: absolute; inset: 0; }
  .brand {
    position: absolute;
    left: 686px;
    top: 108px;
    width: 185px;
    display: flex;
    flex-direction: column;
    align-items: center;
  }
  .brand-square {
    width: 92px;
    height: 92px;
    background: var(--brand-green);
    border-radius: 6px;
  }
  .brand-name {
    margin-top: 8px;
    font-size: 31px;
    font-weight: 700;
    color: var(--brand-blue);
    letter-spacing: -0.5px;
    line-height: 1;
  }
  .letter-body {
    position: absolute;
    left: 55px;
    top: 322px;
    width: 520px;
    font-size: 16.5px;
    font-weight: 500;
    line-height: 21px;
  }
  .letter-body p { margin-bottom: 21px; }
  .letter-body .salutation { font-weight: 700; margin-bottom: 26px; }
  .letter-body .date { margin-bottom: 22px; }
  .letter-body .closing { margin-bottom: 65px; }
  .footer-contact {
    position: absolute;
    left: 66px;
    top: 1104px;
    font-size: 13px;
    font-weight: 700;
    color: var(--brand-blue);
    white-space: nowrap;
  }
  .footer-contact sup { font-size: 8px; }
  .footer-brand {
    position: absolute;
    left: 690px;
    top: 1124px;
    display: flex;
    align-items: center;
    gap: 10px;
  }
  .footer-brand-square {
    width: 56px;
    height: 56px;
    background: var(--paper);
    border-radius: 4px;
  }
  .footer-brand-name {
    font-size: 24px;
    font-weight: 700;
    color: var(--paper);
    letter-spacing: -0.4px;
  }
</style>
</head>
<body>
<main class="letterhead">
  <svg class="frame-shapes" width="927" height="1200" viewBox="0 0 927 1200" aria-hidden="true">
    <rect x="0" y="0" width="927" height="9" fill="var(--brand-blue)"/>
    <polygon points="0,0 108,0 0,116" fill="var(--brand-blue)"/>
    <polygon points="682,1104 927,1104 927,1200 604,1200" fill="var(--brand-blue)"/>
    <rect x="0" y="1191" width="927" height="9" fill="var(--brand-blue)"/>
  </svg>

  <header class="brand">
    <div class="brand-square"></div>
    <div class="brand-name">BrightRoom</div>
  </header>

  <section class="letter-body">
    <p class="date">April 16, 2014</p>
    <p class="salutation">Dear Studio Circle Designers</p>
    <p>I need a letter head designed<br>based on my company logo that I attached.</p>
    <p>Include</p>
    <p>Phone number: (403) 582-4316<br>Address: 347 14th Avenue NE, Calgary, Alberta,<br>Canada, T3K 4R8</p>
    <p class="closing">Thank You,</p>
    <p>BrightRoom Interiors Corporation Team</p>
  </section>

  <footer>
    <div class="footer-contact">347 14<sup>th</sup> Avenue NE, Calgary, Alberta, Canada T3K 4R8 / (403) 582 4316</div>
    <div class="footer-brand">
      <div class="footer-brand-square"></div>
      <div class="footer-brand-name">BrightRoom</div>
    </div>
  </footer>
</main>
</body>
</html>
```